Business Card Design

We are a radiology group

We are working to move into new service centers

We want to communicate innovation and bringing our customers ahead with technology and outstanding results
Updates

I have uploaded a high resolution logo as requested :-)

Target Market(s)

hospitals, clinics

Industry/Entity Type

Business

Contact Information for Business Card

Deborah L. Pettigrew, MBA, CIIP
CTIO
deborah.pettigrew@tdrpc-mail.com
cell 518-476-2913
www.tdrpc-mail.com
Tidewater Diagnostic Radiology, PC

```html
<!DOCTYPE html>
<html lang="en">
<head>
<meta charset="utf-8">
<title>Tidewater Diagnostic Radiology — Business Card</title>
<link rel="stylesheet" href="https://fonts.googleapis.com/css2?family=Open+Sans:wght@400;600&display=swap">
<style>
  :root {
    --page: #ece9e4;
    --card: #ffffff;
    --brand-grey: #6b6b6b;
    --ink: #3a3a3a;
    --accent-blue: #3d8fd6;
    --mark-blue: #a9d8f3;
    --shadow: rgba(0, 0, 0, 0.18);
  }
  * { margin: 0; padding: 0; box-sizing: border-box; }
  html, body {
    width: 1200px;
    height: 1023px;
    overflow: hidden;
    background: var(--page);
    font-family: "Open Sans", Arial, sans-serif;
  }
  .canvas { position: relative; width: 1200px; height: 1023px; }
  .card {
    position: absolute;
    width: 700px;
    height: 400px;
    background: var(--card);
    box-shadow: 0 6px 18px var(--shadow);
  }
  .card--front { left: 70px; top: 70px; }
  .card--back { left: 430px; top: 553px; }

  .brand {
    position: absolute;
    left: 0; right: 0;
    display: flex;
    justify-content: center;
    align-items: center;
    gap: 14px;
  }
  .brand__dot {
    flex: none;
    border-radius: 50%;
    background: var(--mark-blue);
  }
  .brand__name {
    font-weight: 400;
    color: var(--brand-grey);
    white-space: nowrap;
  }
  .card--front .brand { top: 174px; }
  .card--front .brand__dot { width: 22px; height: 22px; }
  .card--front .brand__name { font-size: 34px; }

  .card--back .brand { top: 66px; }
  .card--back .brand__dot { width: 16px; height: 16px; }
  .card--back .brand__name { font-size: 25px; }

  .contact {
    position: absolute;
    left: 70px;
    top: 200px;
  }
  .contact__name {
    font-size: 26px;
    color: var(--ink);
    letter-spacing: 1px;
  }
  .contact__title {
    font-size: 17px;
    color: var(--accent-blue);
    margin-top: 2px;
    letter-spacing: 0.5px;
  }
  .contact__list {
    list-style: none;
    margin-top: 22px;
  }
  .contact__item {
    display: flex;
    align-items: center;
    gap: 10px;
    font-size: 15px;
    color: var(--ink);
    line-height: 26px;
  }
  .contact__item--web { font-weight: 600; }
  .contact__icon { width: 16px; height: 16px; flex: none; }
</style>
</head>
<body>
<main class="canvas">
  <section class="card card--front" aria-label="Card front">
    <div class="brand">
      <span class="brand__dot" aria-hidden="true"></span>
      <p class="brand__name">Tidewater Diagnostic Radiology</p>
    </div>
  </section>

  <section class="card card--back" aria-label="Card back">
    <div class="brand">
      <span class="brand__dot" aria-hidden="true"></span>
      <p class="brand__name">Tidewater Diagnostic Radiology</p>
    </div>
    <div class="contact">
      <p class="contact__name">Deborah L. Pettigrew</p>
      <p class="contact__title">MBA, CIIP CTIO</p>
      <ul class="contact__list">
        <li class="contact__item">
          <svg class="contact__icon" viewBox="0 0 16 16" aria-hidden="true">
            <rect x="0" y="2" width="16" height="12" rx="1.5" fill="#3d8fd6"/>
            <path d="M1 3.5 L8 9 L15 3.5" fill="none" stroke="#fff" stroke-width="1.5"/>
          </svg>
          deborah.pettigrew@tdrpc-mail.com
        </li>
        <li class="contact__item">
          <svg class="contact__icon" viewBox="0 0 16 16" aria-hidden="true">
            <rect x="3" y="0" width="10" height="16" rx="2" fill="#3d8fd6"/>
            <rect x="5" y="2.5" width="6" height="9" fill="#fff"/>
            <circle cx="8" cy="13.6" r="1" fill="#fff"/>
          </svg>
          518-476-2913
        </li>
        <li class="contact__item contact__item--web">
          <svg class="contact__icon" viewBox="0 0 16 16" aria-hidden="true">
            <rect x="1" y="6" width="9" height="5" rx="2.5" transform="rotate(-45 5.5 8.5)" fill="none" stroke="#3d8fd6" stroke-width="1.8"/>
            <rect x="6" y="5" width="9" height="5" rx="2.5" transform="rotate(-45 10.5 7.5)" fill="none" stroke="#3d8fd6" stroke-width="1.8"/>
          </svg>
          www.tdrpc-mail.com
        </li>
      </ul>
    </div>
  </section>
</main>
</body>
</html>
```